Website Homepage Design

Daltrove Care Partners Inc. is a Canadian financial services company that specialize in the delivery and administration of alternative health benefit solutions. Daltrove is seeking to adjust their brand and develop a new website.

We like the design and layout of the website below but are not looking for an exact replica (be creative):

http://www.quellaretreat.example/

We want the colour scheme to be clean white and "fresh green", possibly with orange accents (links).

This posting is only for a website homepage design (no coding), but anyone who includes a new logo, in addition to the design, will get priority.

Best of luck,

Oliver
Updates

Project is guaranteed.

Please let me know if you are currently working on a design.

Thank you,

Oliver

*Update:

Two example websites with good colour scheme/design:

- http://budlynest.example/
- http://www.petalkinderhaus.example.au/

I have attached a wireframe and colour scheme to the project brief. The main colour should be the green one. Other colours can be used for highlights and accents, etc.

Target Market(s)

Business owners age 50+

Industry/Entity Type

Financial

Requirements
Must have
• - Clear and simple design
- Area for video (similar to http://www.quellaretreat.example)
Should not have
• - Lots of pictures

```html
<!DOCTYPE html>
<html lang="en">
<head>
<meta charset="utf-8">
<title>Daltrove Care Partners Inc. – Home</title>
<link rel="stylesheet" href="https://fonts.googleapis.com/css2?family=Arimo:wght@400;700&display=swap">
<style>
  :root {
    --orange: #f26b1d;
    --orange-light: #f7913a;
    --green: #8cc63f;
    --green-dark: #6fa82a;
    --green-active: #79b12f;
    --blue: #2c7fd1;
    --blue-light: #5fb0ec;
    --ink: #333333;
    --grey-text: #555555;
    --grey-mid: #7a7a7a;
    --band: #c9c9c9;
    --panel-frame: #bdbdbd;
    --night: #0b131b;
    --white: #ffffff;
  }
  * { box-sizing: border-box; margin: 0; padding: 0; }
  html, body { width: 1200px; height: 1124px; overflow: hidden; }
  body { position: relative; background: var(--white); font-family: "Arimo", Arial, sans-serif; color: var(--ink); }
  a { text-decoration: none; color: inherit; }

  .utility-bar { position: absolute; left: 0; top: 0; width: 1200px; height: 35px;
    background: linear-gradient(var(--orange-light), var(--orange)); }
  .utility-links { position: absolute; right: 28px; top: 0; display: flex; height: 35px; }
  .utility-links a { color: var(--white); font-weight: 700; font-size: 16px; line-height: 35px; padding: 0 14px; }
  .utility-links a + a { border-left: 1px solid rgba(255,255,255,.4); }

  .site-header { position: absolute; left: 0; top: 35px; width: 1200px; height: 123px; }
  .brand { position: absolute; left: 29px; top: 36px; }
  .brand-name { font-size: 44px; font-weight: 700; color: var(--grey-mid); line-height: 1; letter-spacing: -0.5px; }
  .brand-tagline { font-size: 13px; color: var(--grey-text); margin-top: 8px; }
  .brand-tagline em { font-style: normal; color: var(--orange); }

  .contact-strip { position: absolute; right: 32px; top: 58px; display: flex; align-items: center; gap: 18px;
    font-size: 23px; color: var(--grey-mid); }
  .contact-item { display: flex; align-items: center; gap: 10px; }
  .contact-phone { font-weight: 700; }

  .main-nav { position: absolute; left: 0; top: 158px; width: 1200px; height: 47px;
    background: linear-gradient(var(--green), var(--green-dark)); }
  .main-nav ul { list-style: none; display: flex; padding-left: 14px; height: 47px; }
  .main-nav a { display: block; color: var(--white); font-weight: 700; font-size: 14px; line-height: 47px; padding: 0 29px; }
  .main-nav .is-current a { background: var(--green-active); }

  .video-stage { position: absolute; left: 29px; top: 217px; width: 1138px; height: 452px; background: var(--night); }
  .video-backdrop { position: absolute; inset: 0; background: radial-gradient(circle at 50% 50%, #17222d, var(--night)); }
  .video-frame { position: absolute; left: 299px; top: 0; width: 542px; height: 452px; background: #000; }
  .video-play { position: absolute; left: 226px; top: 178px; }
  .video-channel { position: absolute; right: 12px; bottom: 42px; color: #8a8a8a; font-weight: 700; font-size: 22px; }
  .video-controls { position: absolute; left: 0; bottom: 0; width: 542px; height: 30px;
    background: linear-gradient(#f4f4f4, #cfcfcf); display: flex; align-items: center; font-size: 13px; color: #222; }
  .video-track { width: 280px; height: 6px; background: #aaa; border-radius: 3px; margin: 0 20px 0 10px; }

  .feature-card { position: absolute; top: 681px; width: 373px; height: 153px; color: var(--white); text-align: right; padding: 18px 13px 0 0; }
  .feature-card h2 { font-size: 28px; font-weight: 700; text-shadow: 0 1px 2px rgba(0,0,0,.25); }
  .feature-card p { font-size: 24px; line-height: 30px; margin-top: 20px; }
  .card-process p { margin-top: 40px; }
  .card-savings { left: 29px; background: linear-gradient(var(--blue-light), var(--blue)); }
  .card-process { left: 412px; background: linear-gradient(#a3d45a, var(--green-dark)); }
  .card-question { left: 796px; background: linear-gradient(var(--orange-light), var(--orange)); }
  .card-art { position: absolute; left: 14px; top: 14px; width: 120px; height: 125px; border-radius: 6px; }
  .card-savings .card-art { background: linear-gradient(#8ee06a, #f3d36b); }
  .card-process .card-art { background: #f5f5f5; width: 104px; top: 12px; height: 130px; }
  .card-question .card-art { background: radial-gradient(circle, #ffb347, #e25a00); border-radius: 50%; width: 130px; height: 130px; top: 12px; }

  .info-band { position: absolute; left: 0; top: 845px; width: 1200px; height: 211px;
    background: linear-gradient(var(--band), #e9e9e9); }
  .info-panel { position: absolute; top: 17px; width: 373px; height: 182px; background: var(--white);
    border: 6px solid var(--panel-frame); padding: 10px 16px; overflow: hidden; }
  .info-panel h3 { font-size: 23px; font-weight: 700; color: var(--ink); margin-bottom: 8px; }
  .info-panel p { font-size: 14px; line-height: 17.5px; color: var(--ink); white-space: nowrap; }
  .info-panel p + p { margin-top: 17px; }
  .panel-about { left: 29px; }
  .panel-testimonials { left: 412px; }
  .panel-follow { left: 796px; }
  .more-tab { position: absolute; right: -6px; bottom: -6px; width: 82px; height: 40px;
    background: var(--grey-mid); border-top-left-radius: 40px; color: var(--white); font-weight: 700; font-size: 16px;
    text-align: right; padding: 14px 10px 0 0; }
  .social-list { display: flex; justify-content: space-between; margin-top: 14px; padding: 0 6px; }
  .social-item { text-align: center; font-size: 13px; font-weight: 700; color: var(--grey-text); }
  .social-dot { width: 78px; height: 78px; border-radius: 50%; margin: 0 auto 6px; }
  .dot-a { background: #2e4f8f; } .dot-b { background: #5fc1ea; } .dot-c { background: #b9b9b9; }

  .site-footer { position: absolute; left: 0; top: 1056px; width: 1200px; height: 68px;
    border-top: 1px solid #bbb; background: linear-gradient(#e6e6e6, var(--white));
    text-align: center; font-size: 14px; color: var(--grey-text); padding-top: 30px; }
</style>
</head>
<body>
  <div class="utility-bar">
    <nav class="utility-links"><a href="#">Login</a><a href="#">Singup</a></nav>
  </div>

  <header class="site-header">
    <div class="brand">
      <div class="brand-name">Daltrove</div>
      <div class="brand-tagline">We make it <em>easy</em>. We make it <em>affordable</em>.</div>
    </div>
    <div class="contact-strip">
      <div class="contact-item contact-phone">
        <svg width="38" height="28" viewBox="0 0 38 28"><path d="M2 8c0-5 34-5 34 0v4h-9V8H11v4H2z" fill="#7a7a7a"/><rect x="8" y="13" width="22" height="14" rx="2" fill="#7a7a7a"/></svg>
        604.555.0192
      </div>
      <div class="contact-item">
        <svg width="46" height="28" viewBox="0 0 46 28"><rect x="1" y="1" width="44" height="26" fill="#7a7a7a"/><path d="M1 1l22 15L45 1" fill="none" stroke="#fff" stroke-width="2"/></svg>
        info@daltrove.example
      </div>
    </div>
  </header>

  <nav class="main-nav">
    <ul>
      <li><a href="#">HOME</a></li>
      <li class="is-current"><a href="#">ABOUT DALTROVE</a></li>
      <li><a href="#">CORPORATED</a></li>
      <li><a href="#">INCORPORATED</a></li>
      <li><a href="#">EXCLUSIVE BENEFITS</a></li>
      <li><a href="#">FORMS</a></li>
      <li><a href="#">CONTACT</a></li>
    </ul>
  </nav>

  <section class="video-stage">
    <div class="video-backdrop" role="img" aria-label="Dark starry night backdrop"></div>
    <div class="video-frame">
      <svg class="video-play" width="90" height="64" viewBox="0 0 90 64"><rect x="1" y="1" width="88" height="62" rx="10" fill="#9a9a9a" stroke="#ddd" stroke-width="2"/><path d="M36 18l24 14-24 14z" fill="#222"/></svg>
      <div class="video-channel">Vidora</div>
      <div class="video-controls">
        <svg width="34" height="30" viewBox="0 0 34 30"><path d="M12 8l12 7-12 7z" fill="#222"/></svg>
        <div class="video-track"></div>
        <span>0:00 / 0:00</span>
      </div>
    </div>
  </section>

  <a class="feature-card card-savings" href="#">
    <div class="card-art" role="img" aria-label="Calculator and green folder illustration"></div>
    <h2>REDUCE COSTS</h2><p>Calculate Your<br>Savings</p>
  </a>
  <a class="feature-card card-process" href="#">
    <div class="card-art" role="img" aria-label="Brochure cover preview"></div>
    <h2>HOW IT WORKS</h2><p>View Brochure</p>
  </a>
  <a class="feature-card card-question" href="#">
    <div class="card-art" role="img" aria-label="Orange question mark speech bubble"></div>
    <h2>QUESTION</h2><p>Question<br>Contact us Today</p>
  </a>

  <section class="info-band">
    <article class="info-panel panel-about">
      <h3>ABOUT DALTROVE</h3>
      <p>We're a Canadian financial services company with<br>our head office in Vancouver. We specialize in the<br>delivery and administration of alternative health<br>benefit solutions. We respond to the needs of<br>companies with one to 2500 employees who are<br>looking to control their health..</p>
      <div class="more-tab">More</div>
    </article>
    <article class="info-panel panel-testimonials">
      <h3>TESTIMONIALS</h3>
      <p>Lorem Ipsum dolor sit Lorem Ipsum dolor sit<br>Lorem Ipsum dolor sit&nbsp; Lorem Ipsum dolor sit<br>Lorem Ipsum dolor sit</p>
      <p>Lorem Ipsum dolor sit Lorem Ipsum dolor sit<br>Lorem Ipsum dolor sit</p>
      <div class="more-tab">More</div>
    </article>
    <article class="info-panel panel-follow">
      <h3>FOLLOW WITH US</h3>
      <div class="social-list">
        <div class="social-item"><div class="social-dot dot-a"></div>Friendlane</div>
        <div class="social-item"><div class="social-dot dot-b"></div>Chirply</div>
        <div class="social-item"><div class="social-dot dot-c"></div>Vidora</div>
      </div>
    </article>
  </section>

  <footer class="site-footer">Footer Content here</footer>
</body>
</html>
```